New business card for UK roofing company

We are Brindmore Roofing and we need a business card design for our staff.

We offer the following services:

- New roofs
- General roof repairs
- Drone surveys
- Single ply roofing
- Steel cladding
- Asbestos removal
- Electronic leak detection

I have attached our logo. I have also attached example branding printed to our vans. The business card should fit in with the style of our branding.

The business card should have the following information;

Address:
Unit 17c Wendlecroft Farm
Wendlecroft Lane
Hatchington
CM4 9QD

Telephone: 020 7946 0372
24 Hour: 0800 612 4479

Email: ray@brindmoreroofing.example
Mobile: 07700981234
Name: Ray Tunstead
Website: www.brindmoreroofing.example

The business card will be printed in Spot UV, see here: https://www.kestaprint.example/business-cards/spot-uv/

If you need anymore info, please let me know,

```html
<!DOCTYPE html>
<html lang="en">
<head>
<meta charset="utf-8">
<title>Brindmore Roofing – Business Card</title>
<link href="https://fonts.googleapis.com/css2?family=Poppins:wght@400;500;600;700;800&display=swap" rel="stylesheet">
<style>
  :root {
    --navy: #134f7e;
    --navy-dark: #1a4c7c;
    --sky: #15a8de;
    --ink: #2f3338;
    --paper: #f7f7f7;
    --backdrop: #dedede;
    --rule: #9aa0a6;
  }
  * { box-sizing: border-box; margin: 0; padding: 0; }
  html, body {
    width: 1200px; height: 930px; overflow: hidden;
    background: var(--backdrop);
    font-family: "Poppins", sans-serif;
  }
  .sheet {
    width: 1200px; height: 930px;
    display: flex; flex-direction: column;
    align-items: center; justify-content: center; gap: 56px;
  }
  .card {
    width: 620px; height: 376px;
    box-shadow: 0 6px 18px rgba(0,0,0,.12);
    position: relative;
  }
  .brand {
    display: flex; align-items: center; gap: 12px;
  }
  .brand-name {
    font-weight: 800; font-size: 40px; letter-spacing: -1.5px;
    line-height: 1;
  }
  .brand-dot {
    width: 40px; height: 40px; border-radius: 50%;
  }

  /* front */
  .card-front { background: var(--paper); }
  .card-front .brand { position: absolute; left: 150px; top: 58px; }
  .card-front .brand-name { color: var(--sky); }
  .card-front .brand-dot { background: var(--navy-dark); }
  .holder {
    position: absolute; left: 0; right: 0; top: 128px;
    text-align: center; font-weight: 700; font-size: 24px;
  }
  .holder .first { color: var(--navy-dark); }
  .holder .last { color: var(--sky); }
  .details {
    position: absolute; left: 40px; right: 30px; top: 196px;
    display: flex; align-items: stretch;
  }
  .address {
    flex: 0 0 250px; text-align: right; padding-right: 20px;
    font-size: 15px; line-height: 1.42; color: var(--ink);
  }
  .address .hotline { color: var(--sky); margin-top: 2px; }
  .address .hotline b { font-weight: 400; color: var(--navy-dark); }
  .divider { width: 1px; background: var(--rule); }
  .contacts {
    list-style: none; padding-left: 20px;
    font-size: 15px; line-height: 1.42; color: var(--ink);
  }
  .contacts li { display: flex; align-items: center; gap: 9px; }
  .contacts svg { width: 15px; height: 15px; flex: none; }

  /* back */
  .card-back {
    background: var(--navy);
    display: flex; flex-direction: column; align-items: center; justify-content: center;
    text-align: center;
  }
  .card-back .brand-name { color: #ffffff; }
  .card-back .brand-dot { background: var(--sky); }
  .services-title {
    margin-top: 26px; color: var(--sky);
    font-weight: 700; font-size: 15px; letter-spacing: .3px;
  }
  .services {
    margin-top: 4px; color: #ffffff;
    font-size: 16px; line-height: 1.45;
  }
</style>
</head>
<body>
<main class="sheet">

  <section class="card card-front" aria-label="Business card front">
    <div class="brand">
      <span class="brand-name">Brindmore Roofing</span>
      <span class="brand-dot"></span>
    </div>
    <p class="holder"><span class="first">Ray</span> <span class="last">Tunstead</span></p>
    <div class="details">
      <address class="address">
        Unit 17c Wendlecroft Farm<br>
        Wendlecroft Lane<br>
        Hatchington, CM4 9QD
        <div class="hotline">24 Hour: <b>0800 612 4479</b></div>
      </address>
      <div class="divider"></div>
      <ul class="contacts">
        <li>
          <svg viewBox="0 0 16 16" aria-hidden="true"><rect x="4" y="1" width="8" height="14" rx="1.5" fill="none" stroke="#15a8de" stroke-width="1.5"/><circle cx="8" cy="12.5" r=".9" fill="#15a8de"/></svg>
          07700981234
        </li>
        <li>
          <svg viewBox="0 0 16 16" aria-hidden="true"><path d="M4 1.5l2.3 3-1.4 1.7c.8 1.9 2.2 3.3 4.1 4.1l1.7-1.4 3 2.3-1.6 2.6C6.7 13.8 2.2 9.3 1.4 4z" fill="#15a8de"/></svg>
          020 7946 0372
        </li>
        <li>
          <svg viewBox="0 0 16 16" aria-hidden="true"><rect x="1" y="3" width="14" height="10" rx="1" fill="#15a8de"/><path d="M1.5 3.8L8 9l6.5-5.2" fill="none" stroke="#fff" stroke-width="1.2"/></svg>
          ray@brindmoreroofing.example
        </li>
        <li>
          <svg viewBox="0 0 16 16" aria-hidden="true"><circle cx="8" cy="8" r="6.5" fill="#15a8de"/><path d="M1.5 8h13M8 1.5c-3 3.5-3 9.5 0 13M8 1.5c3 3.5 3 9.5 0 13" fill="none" stroke="#fff" stroke-width="1"/></svg>
          www.brindmoreroofing.example
        </li>
      </ul>
    </div>
  </section>

  <section class="card card-back" aria-label="Business card back">
    <div class="brand">
      <span class="brand-name">Brindmore Roofing</span>
      <span class="brand-dot"></span>
    </div>
    <h2 class="services-title">WE OFFER THE FOLLOWING SERVICES:</h2>
    <p class="services">
      New roofs | General roof repairs | Drone surveys<br>
      Single ply roofing | Steel cladding<br>
      Asbestos removal | Electronic leak detection
    </p>
  </section>

</main>
</body>
</html>
```